Professional looking Roller Blind Discount Card that portrays quality at a value for money price!

We need a double sided business card designed as a discount card. Size 90mm wide x 55mm high.We would like it to look professional and portray quality at a value for money price point.I have uploaded a word document with a basic layout with the information we want included on each side of the card. Please put your own thought into the layout.

Contact Information for Business Card

As per word document attached.

```html
<!DOCTYPE html>
<html lang="en">
<head>
<meta charset="utf-8">
<title>Kestrel Interiors – Roller Blind Discount Card</title>
<link href="https://fonts.googleapis.com/css2?family=Lato:wght@300;400;700;900&display=swap" rel="stylesheet">
<style>
  :root {
    --blue: #29a8dd;
    --blue-deep: #1f93c4;
    --ink: #5a4e4a;
    --ink-dark: #3a3a3a;
    --grey-band: #6b6a69;
    --white: #ffffff;
    --page: #e9e9e7;
  }
  * { box-sizing: border-box; margin: 0; padding: 0; }
  html, body { width: 1200px; height: 900px; overflow: hidden; }
  body {
    background: var(--page);
    font-family: 'Lato', sans-serif;
    position: relative;
  }
  .card {
    position: absolute;
    left: 280px;
    width: 640px;
    height: 391px;
    background: var(--white);
    overflow: hidden;
    box-shadow: 0 6px 18px rgba(0,0,0,.18);
  }
  .card--back { top: 40px; }
  .card--front { top: 469px; }

  /* ---------- back side ---------- */
  .back-photo {
    position: absolute; inset: 0 0 150px 0;
    background: linear-gradient(120deg, #efefed 0%, #dedfdb 45%, #c9cdc5 100%);
  }
  .back-band {
    position: absolute; left: 0; right: 0; bottom: 0; height: 165px;
    background: var(--grey-band);
  }
  .offer-bubble { position: absolute; left: 36px; top: 62px; width: 116px; height: 118px; }
  .offer-bubble__text {
    position: absolute; left: 0; top: 12px; width: 116px; text-align: center;
    color: var(--white); font-weight: 900; font-size: 36px; line-height: 34px;
  }
  .back-headline { position: absolute; left: 172px; top: 70px; }
  .back-headline__title { color: var(--blue); font-weight: 700; font-size: 23px; }
  .back-headline__types { color: var(--ink-dark); font-weight: 400; font-size: 23px; margin-top: 4px; word-spacing: 3px; }

  .seal { position: absolute; width: 100px; height: 100px; }
  .seal svg { position: absolute; inset: 0; width: 100px; height: 100px; }
  .seal__small {
    position: absolute; left: 0; width: 100px; text-align: center;
    font-size: 6px; font-weight: 700; letter-spacing: 1px; color: var(--ink-dark);
  }
  .seal__small--top { top: 25px; }
  .seal__small--bottom { top: 68px; }
  .seal__label {
    position: absolute; left: 0; top: 42px; width: 100px; text-align: center;
    color: var(--white); font-weight: 700; font-size: 12px; line-height: 16px; letter-spacing: 1.2px;
  }
  .seal__label--long { font-size: 9.5px; letter-spacing: .8px; }
  .seal--free { left: 60px; top: 222px; }
  .seal--price { left: 195px; top: 182px; }
  .seal--family { left: 345px; top: 142px; }

  /* ---------- call pill (shared) ---------- */
  .call {
    position: absolute; right: 26px; bottom: 34px; width: 300px; height: 96px;
  }
  .call__pill {
    position: absolute; left: 0; top: 12px; width: 250px; height: 72px;
    background: var(--white); border-radius: 36px;
    box-shadow: 0 2px 6px rgba(0,0,0,.15);
    padding: 8px 0 0 26px;
  }
  .call__label {
    color: var(--ink); font-size: 20px; font-weight: 400;
    width: 180px; text-align: center; border-bottom: 1px solid #9a9390; padding-bottom: 2px;
  }
  .call__number { color: var(--blue); font-size: 25px; font-weight: 700; letter-spacing: 1px; margin-top: 1px; }
  .call__icon {
    position: absolute; right: 0; top: 0; width: 96px; height: 96px; border-radius: 50%;
    background: var(--blue); border: 6px solid var(--white);
    display: flex; align-items: center; justify-content: center;
    box-shadow: 0 2px 6px rgba(0,0,0,.15);
  }

  /* ---------- front side ---------- */
  .front-photo {
    position: absolute; left: 200px; top: 130px; width: 440px; height: 261px;
    background: linear-gradient(100deg, #5f6e55 0%, #8a9a7c 40%, #c8c7bf 75%, #e2e0da 100%);
  }
  .front-grey {
    position: absolute; left: 0; top: 200px; width: 200px; height: 191px;
    background: var(--grey-band);
  }
  .front-wave { position: absolute; inset: 0; }
  .brand {
    position: absolute; left: 34px; top: 40px; width: 200px;
    display: flex; flex-direction: column; align-items: center; gap: 10px;
  }
  .brand__mark { width: 30px; height: 30px; background: var(--blue); }
  .brand__name { color: var(--blue-deep); font-weight: 700; font-size: 18px; letter-spacing: .5px; white-space: nowrap; }
  .headline { position: absolute; right: 36px; top: 50px; text-align: right; }
  .headline__title { color: var(--ink); font-weight: 900; font-size: 54px; line-height: 56px; letter-spacing: -.5px; white-space: nowrap; }
  .headline__sub { color: var(--blue); font-weight: 700; font-size: 19px; margin-top: 2px; }
  .fabric-badge {
    position: absolute; left: 66px; top: 168px; width: 168px; height: 168px; border-radius: 50%;
    background: var(--blue); border: 6px solid var(--white);
    box-shadow: 0 3px 8px rgba(0,0,0,.2);
    display: flex; align-items: center; justify-content: center; text-align: center;
    color: var(--white); font-size: 23px; font-weight: 400; line-height: 27px;
  }
</style>
</head>
<body>

<section class="card card--back" aria-label="Card back">
  <div class="back-photo" role="img" aria-label="Photo of a bright room with roller blinds over garden windows"></div>
  <div class="back-band"></div>

  <div class="offer-bubble">
    <svg width="116" height="118" viewBox="0 0 116 118">
      <path d="M12 0 H104 A12 12 0 0 1 116 12 V84 A12 12 0 0 1 104 96 H70 L58 116 L46 96 H12 A12 12 0 0 1 0 84 V12 A12 12 0 0 1 12 0 Z" fill="var(--blue)"/>
    </svg>
    <div class="offer-bubble__text">25%<br>OFF</div>
  </div>

  <div class="back-headline">
    <p class="back-headline__title">Quality Custom Made Roller Blinds</p>
    <p class="back-headline__types">Blockout | Screen | Light Filtering</p>
  </div>

  <div class="seal seal--free">
    <svg viewBox="0 0 118 118"><circle cx="59" cy="59" r="56" fill="var(--blue)"/><circle cx="59" cy="59" r="46" fill="none" stroke="#fff" stroke-width="2"/><path d="M-4 46 H122 L114 59 L122 72 H-4 L4 59 Z" fill="#2d2d2d"/></svg>
    <div class="seal__small seal__small--top">IN HOME</div>
    <div class="seal__label">FREE</div>
    <div class="seal__small seal__small--bottom">QUOTE</div>
  </div>
  <div class="seal seal--price">
    <svg viewBox="0 0 118 118"><circle cx="59" cy="59" r="56" fill="var(--blue)"/><circle cx="59" cy="59" r="46" fill="none" stroke="#fff" stroke-width="2"/><path d="M-4 46 H122 L114 59 L122 72 H-4 L4 59 Z" fill="#2d2d2d"/></svg>
    <div class="seal__small seal__small--top">GUARANTEED</div>
    <div class="seal__label">BEST PRICE</div>
    <div class="seal__small seal__small--bottom">LOWEST</div>
  </div>
  <div class="seal seal--family">
    <svg viewBox="0 0 118 118"><circle cx="59" cy="59" r="56" fill="var(--blue)"/><circle cx="59" cy="59" r="46" fill="none" stroke="#fff" stroke-width="2"/><path d="M-4 46 H122 L114 59 L122 72 H-4 L4 59 Z" fill="#2d2d2d"/></svg>
    <div class="seal__small seal__small--top">LOCALLY</div>
    <div class="seal__label seal__label--long">FAMILY OWNED</div>
    <div class="seal__small seal__small--bottom">OPERATED</div>
  </div>

  <div class="call">
    <div class="call__pill">
      <p class="call__label">Call Today</p>
      <p class="call__number">0400 555 218</p>
    </div>
    <div class="call__icon">
      <svg width="44" height="44" viewBox="0 0 24 24"><path fill="#fff" d="M6.6 10.8c1.4 2.8 3.8 5.1 6.6 6.6l2.2-2.2c.3-.3.7-.4 1-.2 1.1.4 2.3.6 3.6.6.6 0 1 .4 1 1V20c0 .6-.4 1-1 1C10.6 21 3 13.4 3 4c0-.6.4-1 1-1h3.5c.6 0 1 .4 1 1 0 1.3.2 2.5.6 3.6.1.3 0 .7-.2 1L6.6 10.8z"/></svg>
    </div>
  </div>
</section>

<section class="card card--front" aria-label="Card front">
  <div class="front-photo" role="img" aria-label="Photo of a living room window with a roller blind and garden view"></div>
  <div class="front-grey"></div>
  <svg class="front-wave" width="640" height="391" viewBox="0 0 640 391">
    <path d="M0 0 H640 V142 C520 140 390 162 270 200 C170 232 80 255 0 268 Z" fill="var(--blue)"/>
    <path d="M0 0 H640 V128 C520 126 390 148 270 186 C170 218 80 243 0 256 Z" fill="var(--white)"/>
  </svg>

  <div class="brand">
    <span class="brand__mark"></span>
    <span class="brand__name">KESTREL INTERIORS</span>
  </div>

  <div class="headline">
    <h1 class="headline__title">Roller Blinds</h1>
    <p class="headline__sub">FREE in Home Measure &amp; Quote</p>
  </div>

  <div class="fabric-badge">Huge<br>Selection<br>Of Fabrics</div>

  <div class="call">
    <div class="call__pill">
      <p class="call__label">Call Today</p>
      <p class="call__number">0400 555 218</p>
    </div>
    <div class="call__icon">
      <svg width="44" height="44" viewBox="0 0 24 24"><path fill="#fff" d="M6.6 10.8c1.4 2.8 3.8 5.1 6.6 6.6l2.2-2.2c.3-.3.7-.4 1-.2 1.1.4 2.3.6 3.6.6.6 0 1 .4 1 1V20c0 .6-.4 1-1 1C10.6 21 3 13.4 3 4c0-.6.4-1 1-1h3.5c.6 0 1 .4 1 1 0 1.3.2 2.5.6 3.6.1.3 0 .7-.2 1L6.6 10.8z"/></svg>
    </div>
  </div>
</section>

</body>
</html>
```